Business Card Design Project 4 Construction Business

I am after a creative, but sleek and simple/ clean business card design. This design will form the basis of future items and might include a logo or simply a creative way to lay out the text of my company name 'keldmoor builds'
I like the simplicity of black and white however I would also be happy to see a splash of colour introduced somehow to give the text some interest and make it stand out.
I would like a double sided card.
I am young (ish!) and professional, offering construction and project management services, what I don't want is the traditional builders type card featuring a cheesy hammer/ saw image etc.
As the company name, keldmoor builds, suggests, we focus on working closely and collaboratively together, in synergy with all stakeholders involved in the projects that we undertake
Industry/Entity Type
Construction

```html
<!DOCTYPE html>
<html lang="en">
<head>
<meta charset="utf-8">
<title>Keldmoor Builds – Business Card</title>
<link rel="stylesheet" href="https://fonts.googleapis.com/css2?family=Mulish:wght@400;600;800&display=swap">
<style>
  :root {
    --stage: #2b2b2b;
    --ink: #1a1a1a;
    --ink-deep: #0d0d0d;
    --ink-soft: #262626;
    --signal: #ffdd00;
  }
  * { margin: 0; padding: 0; box-sizing: border-box; }
  html, body { width: 1200px; height: 900px; overflow: hidden; }
  body {
    background: var(--stage);
    font-family: "Mulish", sans-serif;
    position: relative;
  }
  .card {
    position: absolute;
    top: 307px;
    width: 514px;
    height: 286px;
    border-radius: 18px;
    overflow: hidden;
  }
  .card--front {
    left: 73px;
    background: linear-gradient(100deg, var(--ink-deep) 0%, var(--ink-soft) 100%);
    display: flex;
    align-items: center;
    justify-content: center;
  }
  .card--back {
    left: 615px;
    background: var(--signal);
  }
  .wordmark {
    font-weight: 800;
    text-transform: uppercase;
    text-align: center;
    line-height: 1.05;
  }
  .wordmark--front {
    color: var(--signal);
    font-size: 38px;
    letter-spacing: 1px;
  }
  .wordmark--front span { display: block; font-size: 22px; letter-spacing: 9px; }
  .wordmark--back {
    position: absolute;
    left: 42px;
    top: 70px;
    color: var(--ink);
    font-size: 27px;
    letter-spacing: 0.5px;
  }
  .wordmark--back span { display: block; font-size: 16px; letter-spacing: 6px; }
  .holder {
    position: absolute;
    right: 42px;
    top: 76px;
    text-align: right;
    color: var(--ink);
  }
  .holder__name { font-size: 19px; font-weight: 400; }
  .holder__role { font-size: 14px; margin-top: 4px; }
  .back-band {
    position: absolute;
    left: 0; top: 0;
    width: 514px; height: 286px;
  }
  .address {
    position: absolute;
    left: 43px;
    top: 232px;
    color: var(--signal);
    font-size: 11.5px;
    line-height: 17px;
  }
  .contacts {
    position: absolute;
    right: 42px;
    top: 214px;
    list-style: none;
    color: var(--signal);
    font-size: 11.5px;
    line-height: 17px;
    text-align: right;
  }
  .contacts li { display: flex; align-items: center; justify-content: flex-end; gap: 6px; }
  .contacts .phone { font-weight: 800; }
  .contacts svg { width: 10px; height: 10px; flex: none; }
</style>
</head>
<body>
  <section class="card card--front" aria-label="Card front">
    <h1 class="wordmark wordmark--front">Keldmoor<span>Builds</span></h1>
  </section>

  <section class="card card--back" aria-label="Card back">
    <svg class="back-band" viewBox="0 0 514 286" aria-hidden="true">
      <path d="M0 188 C 160 200, 360 186, 514 164 L514 286 L0 286 Z" fill="var(--ink)"/>
      <path d="M0 182 C 170 192, 360 178, 514 158" fill="none" stroke="var(--ink)" stroke-width="2.5"/>
    </svg>

    <h2 class="wordmark wordmark--back">Keldmoor<span>Builds</span></h2>

    <div class="holder">
      <p class="holder__name">Tobias Wren</p>
      <p class="holder__role">Director</p>
    </div>

    <address class="address" style="font-style:normal">14 Larkin St<br>Harwood NSW 2071</address>

    <ul class="contacts">
      <li class="phone">0412 555 018
        <svg viewBox="0 0 10 10"><circle cx="5" cy="5" r="5" fill="var(--signal)"/><path d="M3.2 2.6 l1 1 -0.5 0.7 c0.4 0.8 0.9 1.3 1.6 1.6 l0.7 -0.5 1 1 -0.8 0.9 C4.6 7.1 2.9 5.4 2.3 3.4 Z" fill="var(--ink)"/></svg>
      </li>
      <li>tobias@keldmoorbuilds.com.au
        <svg viewBox="0 0 10 10"><rect x="0.5" y="2" width="9" height="6.5" fill="var(--signal)"/><path d="M0.5 2 L5 5.6 L9.5 2" fill="none" stroke="var(--ink)" stroke-width="0.9"/></svg>
      </li>
      <li>www.keldmoorbuilds.com.au
        <svg viewBox="0 0 10 10"><circle cx="5" cy="5" r="4.5" fill="var(--signal)"/><g fill="none" stroke="var(--ink)" stroke-width="0.7"><ellipse cx="5" cy="5" rx="1.8" ry="4.2"/><path d="M0.8 5 H9.2 M1.6 3 H8.4 M1.6 7 H8.4"/></g></svg>
      </li>
    </ul>
  </section>
</body>
</html>
```